Company Stationery for Contracts, Invoices and other Company Letters | (Briefpapier / Briefkopf)
We are an Online-Shop for different Online Services over different websites.
We have multiple in-game currency sites under our company name.

```html
<!DOCTYPE html>
<html lang="en">
<head>
<meta charset="utf-8">
<title>Quellmark Stationery</title>
<link rel="stylesheet" href="https://fonts.googleapis.com/css2?family=Montserrat:wght@400;500;700&display=swap">
<style>
  :root {
    --bg: #dedbd0;
    --red: #d2232c;
    --red-light: #e3373f;
    --red-dark: #b51c24;
    --paper: #ececec;
    --cream: #ecebe4;
    --ink: #222222;
    --flap-grey: #3a3a3a;
  }
  html, body {
    margin: 0;
    padding: 0;
    width: 1200px;
    height: 900px;
    overflow: hidden;
    background: var(--bg);
    font-family: "Montserrat", sans-serif;
  }
  .canvas {
    position: relative;
    width: 1200px;
    height: 900px;
  }

  /* Letterhead */
  .letterhead {
    position: absolute;
    left: 90px;
    top: 90px;
    width: 500px;
    height: 707px;
    background: var(--paper);
    box-shadow: 0 10px 30px rgba(0,0,0,0.18);
    overflow: hidden;
  }
  .letterhead__field {
    position: absolute;
    left: 0; top: 0;
    width: 100%;
    height: 400px;
    background: linear-gradient(160deg, var(--red-dark) 0%, var(--red) 55%, var(--red-light) 100%);
  }
  .letterhead__edge {
    position: absolute;
    left: 0; top: 400px;
    width: 100%;
    height: 10px;
    background: var(--red-dark);
  }
  .letterhead__brand {
    position: absolute;
    left: 44px;
    top: 440px;
    display: flex;
    align-items: center;
    gap: 12px;
  }
  .brand-square {
    width: 22px;
    height: 22px;
    background: var(--red);
  }
  .brand-name {
    font-weight: 700;
    font-size: 52px;
    line-height: 1;
    color: var(--ink);
    letter-spacing: -0.5px;
  }
  .letterhead__details {
    position: absolute;
    left: 44px;
    top: 518px;
    width: 420px;
    font-size: 11px;
    line-height: 1.4;
    color: var(--ink);
  }
  .detail-group {
    padding: 6px 0;
    border-bottom: 2px solid var(--red);
  }
  .detail-group:last-child { border-bottom: none; }
  .detail-group strong { font-weight: 700; }
  .bank-row { display: flex; gap: 14px; }
  .bank-row .label { font-weight: 700; width: 34px; }

  /* Envelope */
  .envelope {
    position: absolute;
    left: 640px;
    top: 300px;
    width: 480px;
    height: 430px;
  }
  .envelope__shape {
    position: absolute;
    left: 0; top: 0;
  }
  .envelope__brand {
    position: absolute;
    left: 0;
    top: 262px;
    width: 100%;
    display: flex;
    justify-content: center;
    align-items: center;
    gap: 8px;
  }
  .envelope__brand .brand-square { width: 14px; height: 14px; }
  .envelope__brand .brand-name { font-size: 30px; color: #3a3a3a; }
</style>
</head>
<body>
<main class="canvas">

  <section class="letterhead" aria-label="Letterhead">
    <div class="letterhead__field"></div>
    <div class="letterhead__edge"></div>
    <div class="letterhead__brand">
      <span class="brand-square"></span>
      <span class="brand-name">Quellmark</span>
    </div>
    <div class="letterhead__details">
      <div class="detail-group">
        <strong>Quellmark</strong> · Any Street 1<br>
        Any City 12345<br>
        Greece
      </div>
      <div class="detail-group">
        <strong>Nikos Varelidis</strong> · CEO<br>
        <strong>ΑΦΜ</strong> EL999999999
      </div>
      <div class="detail-group">
        Aegean Trust Bank<br>
        <div class="bank-row"><span class="label">IBAN</span><span>GR27 0000 0000 0000 0000 00</span></div>
        <div class="bank-row"><span class="label">BIC</span><span>AGTBGRAAXXX</span></div>
      </div>
    </div>
  </section>

  <section class="envelope" aria-label="Envelope">
    <svg class="envelope__shape" width="480" height="430" viewBox="0 0 480 430">
      <defs>
        <linearGradient id="flapRed" x1="0" y1="0" x2="0" y2="1">
          <stop offset="0" stop-color="#cc2129"/>
          <stop offset="1" stop-color="#d62a32"/>
        </linearGradient>
      </defs>
      <path d="M10 130 L60 18 Q68 4 84 4 L396 4 Q412 4 420 18 L470 130 Z" fill="url(#flapRed)"/>
      <rect x="0" y="130" width="480" height="40" fill="#d52a31"/>
      <path d="M0 130 L30 150 L44 400 L0 420 Z" fill="var(--flap-grey)"/>
      <path d="M480 130 L450 150 L436 400 L480 420 Z" fill="#4a4a4a"/>
      <path d="M34 170 Q36 158 48 158 L432 158 Q444 158 446 170 L478 420 L2 420 Z" fill="var(--cream)"/>
    </svg>
    <div class="envelope__brand">
      <span class="brand-square"></span>
      <span class="brand-name">Quellmark</span>
    </div>
  </section>

</main>
</body>
</html>
```